Marke für hochwertige Trauerartikel benötigt Briefpapier
Zielgruppe
Weidkorn ist eine Marke für hochwertige Trauerartikel. Zielgruppe sind Bestattungsunternehmen, die nachhaltig zufriedenen Kunden möchten.
Aufgabenstellung
Wir benötigen Briefpapier: Anschreiben, Rechnngsformular in Farbe und in schwarz weiß. Dazu Visitenkarten und ein gleicherscheinenden E-Mail Absender. Das Design sollte so klar wir möglich sein. Der Druck erfolgt auf recyceltem Papier.

```html
<!DOCTYPE html>
<html lang="de">
<head>
<meta charset="utf-8">
<title>Weidkorn – Briefpapier</title>
<link href="https://fonts.googleapis.com/css2?family=Open+Sans:wght@400;600;700&display=swap" rel="stylesheet">
<style>
  :root {
    --backdrop: #dcdce0;
    --paper: #f4f5f7;
    --paper-dark: #2f2f2f;
    --gold: #c9a22c;
    --gold-faint: #efe6cf;
    --ink: #1e1e1e;
    --ink-soft: #444;
  }
  * { margin: 0; padding: 0; box-sizing: border-box; }
  html, body { width: 1200px; height: 927px; overflow: hidden; }
  body {
    background: var(--backdrop);
    font-family: "Open Sans", Arial, sans-serif;
    position: relative;
  }
  .sheet {
    position: absolute;
    width: 305px;
    height: 433px;
    background: var(--paper);
    box-shadow: 0 8px 22px rgba(0,0,0,.22);
    overflow: hidden;
  }
  .sheet--framed { left: 66px; top: 220px; }
  .sheet--plain { left: 408px; top: 225px; }
  .sheet--cover { left: 771px; top: 225px; background: var(--paper-dark); height: 436px; }

  .frame {
    position: absolute;
    inset: 12px;
    border: 1.5px solid var(--gold);
  }
  .sheet--cover .frame { inset: 11px; }

  .brand-mark {
    position: absolute;
    display: flex;
    align-items: center;
    gap: 4px;
    font-weight: 700;
    font-size: 10px;
    color: var(--ink);
  }
  .brand-mark__square {
    width: 9px; height: 9px;
    border: 1px solid var(--gold);
  }
  .sheet--framed .brand-mark { left: 36px; top: 54px; }
  .sheet--plain .brand-mark { left: 24px; top: 64px; }

  .deco-area {
    position: absolute;
    background: radial-gradient(ellipse at 100% 50%, var(--gold-faint) 0%, rgba(239,230,207,.45) 55%, rgba(244,245,247,0) 80%);
  }
  .sheet--framed .deco-area { left: 153px; top: 76px; width: 140px; height: 312px; }
  .sheet--plain .deco-area { left: 165px; top: 71px; width: 140px; height: 290px; }

  .footer-centered {
    position: absolute;
    left: 0; right: 0;
    top: 377px;
    text-align: center;
  }
  .company-name { font-weight: 600; font-size: 6.5px; }
  .footer-centered .company-name { color: var(--gold); }
  .legal { font-size: 4.6px; line-height: 7px; color: var(--ink-soft); }
  .footer-centered .legal { margin-top: 6px; }

  .web-on-frame {
    position: absolute;
    left: 0; right: 0;
    text-align: center;
    font-size: 7px;
    color: var(--gold);
  }
  .web-on-frame span { background: var(--paper); padding: 0 6px; }
  .sheet--framed .web-on-frame { top: 415px; }
  .sheet--cover .web-on-frame { top: 419px; }
  .sheet--cover .web-on-frame span { background: var(--paper-dark); font-size: 8px; }

  .footer-left {
    position: absolute;
    left: 21px;
    top: 364px;
  }
  .footer-left .company-name { color: var(--ink); }
  .web-bar {
    display: inline-block;
    margin-top: 3px;
    width: 80px;
    height: 9px;
    line-height: 9px;
    padding-left: 4px;
    background: var(--gold);
    color: #fff;
    font-size: 5.5px;
  }
  .footer-left .legal { margin-top: 3px; }

  .cover-brand {
    position: absolute;
    left: 0; right: 0;
    top: 190px;
    text-align: center;
    font-weight: 700;
    font-size: 24px;
    color: var(--gold);
  }
</style>
</head>
<body>

  <section class="sheet sheet--framed">
    <div class="frame"></div>
    <div class="brand-mark"><span class="brand-mark__square"></span>Weidkorn</div>
    <div class="deco-area" role="img" aria-label="Faint decorative floral pattern"></div>
    <div class="footer-centered">
      <p class="company-name">Weidkorn</p>
      <p class="legal">HR:2741 - St.-Nr.:58302174 - USt:30918462<br>BNR:8130527 - IK:002947163000051<br>Sitz: Lindenweg 12, 37085 Musterfeld</p>
    </div>
    <p class="web-on-frame"><span>www.weidkorn-beispiel.de</span></p>
  </section>

  <section class="sheet sheet--plain">
    <div class="brand-mark"><span class="brand-mark__square"></span>Weidkorn</div>
    <div class="deco-area" role="img" aria-label="Faint decorative floral pattern"></div>
    <div class="footer-left">
      <p class="company-name">Weidkorn</p>
      <span class="web-bar">www.weidkorn-beispiel.de</span>
      <p class="legal">HR:2741 - St.-Nr.:58302174 - USt:30918462<br>BNR:8130527 - IK:002947163000051<br>Sitz: Lindenweg 12, 37085 Musterfeld</p>
    </div>
  </section>

  <section class="sheet sheet--cover">
    <div class="frame"></div>
    <p class="cover-brand">Weidkorn</p>
    <p class="web-on-frame"><span>www.weidkorn-beispiel.de</span></p>
  </section>

</body>
</html>
```